Debt Relief Landing Page Design

I need a landing page designed (and the accompanying Thank You page) for my client.

I have drafted the wireframes for the layout of the pages (attached) and need a professional looking finish.

The main colours to use are green and blue as per their current branding, see website for specifications - http://www.clearpathledger.com.au/

```html
<!DOCTYPE html>
<html lang="en">
<head>
<meta charset="utf-8">
<title>Clear Path Ledger – Debt Relief</title>
<link href="https://fonts.googleapis.com/css2?family=Open+Sans:wght@400;600;700&family=Raleway:wght@400;500;600;700&display=swap" rel="stylesheet">
<style>
:root{
  --green:#6aa51c;
  --green-dark:#4f8412;
  --navy:#1b3257;
  --navy-deep:#12233f;
  --blue-panel:#1d3a66;
  --ink:#333c46;
  --muted:#6f7780;
  --footer:#1c1f24;
  --footer-text:#8b9097;
  --white:#ffffff;
  --line:#e3e6ea;
}
*{box-sizing:border-box;margin:0;padding:0}
html,body{width:1200px;height:2260px;overflow:hidden}
body{font-family:"Open Sans",Arial,sans-serif;color:var(--ink);background:var(--white)}
.page{width:1200px;height:2260px;position:relative}

.site-header{height:112px;display:flex;align-items:center;justify-content:space-between;padding:0 70px}
.brand{display:flex;align-items:center;gap:14px}
.brand-mark{width:22px;height:22px;background:var(--green)}
.brand-name{font-family:"Raleway",sans-serif;font-weight:700;font-size:34px;color:var(--navy)}
.contact{display:flex;align-items:center;gap:12px;font-size:15px;color:var(--navy)}
.contact-icon{width:40px;height:40px;border-radius:50%;background:var(--navy);display:flex;align-items:center;justify-content:center}

.main-nav{height:40px;background:var(--green);display:flex;padding:0 70px}
.main-nav a{color:var(--white);text-decoration:none;font-size:13px;flex:1;display:flex;align-items:center;justify-content:center;border-right:1px solid rgba(255,255,255,.25)}
.main-nav a:first-child{background:var(--navy);flex:0 0 90px}
.main-nav a:last-child{border-right:none}

.hero{height:408px;position:relative;overflow:hidden}
.hero-photo{position:absolute;inset:0;background:linear-gradient(100deg,#2c3e56 0%,#4a5a70 45%,#7d8794 70%,#5f6b7a 100%)}
.hero-shade{position:absolute;inset:0;background:linear-gradient(90deg,rgba(18,35,63,.75),rgba(18,35,63,.35))}
.hero-copy{position:absolute;left:70px;top:70px;width:700px;color:var(--white)}
.hero-copy h1{font-family:"Raleway",sans-serif;font-weight:600;font-size:40px;margin-bottom:26px}
.hero-copy p{font-size:14px;line-height:1.7;margin-bottom:14px;color:#e6ebf2}
.consult-form{position:absolute;right:70px;top:20px;width:290px;height:368px;background:rgba(22,44,80,.92);padding:18px 22px;color:var(--white)}
.consult-form h2{font-family:"Raleway",sans-serif;font-size:20px;font-weight:600;margin-bottom:6px}
.consult-form .intro{font-size:11px;line-height:1.5;color:#c9d3e2;margin-bottom:12px}
.field{display:flex;align-items:center;margin-bottom:8px;font-size:11px}
.field span{width:86px;color:#dfe6f0}
.field i{flex:1;height:26px;background:var(--white);display:block}
.btn{display:inline-block;background:var(--green);color:var(--white);font-size:12px;font-weight:700;letter-spacing:.5px;padding:12px 26px;border-bottom:3px solid var(--green-dark)}
.consult-form .btn{display:block;text-align:center;margin-top:14px;padding:12px 0}

.section-title{font-family:"Raleway",sans-serif;font-weight:500;font-size:38px;text-align:center}
.section-title em{font-style:normal;color:var(--green)}

.services{height:770px;padding-top:76px}
.services .section-title{color:var(--ink);margin-bottom:66px}
.service-grid{display:grid;grid-template-columns:repeat(3,1fr);column-gap:60px;row-gap:50px;padding:0 120px}
.service{text-align:center}
.service-icon{width:62px;height:62px;border-radius:50%;border:2px solid var(--navy);margin:0 auto 16px;display:flex;align-items:center;justify-content:center}
.service h3{font-family:"Raleway",sans-serif;font-weight:600;font-size:17px;color:var(--ink);margin-bottom:10px}
.service p{font-size:12px;line-height:1.6;color:var(--muted)}
.center-cta{text-align:center;margin-top:60px}

.testimonials{height:710px;background:var(--navy);padding-top:70px;position:relative;color:var(--white)}
.testimonials .section-title{margin-bottom:60px}
.quote-grid{display:grid;grid-template-columns:repeat(3,1fr);column-gap:50px;row-gap:44px;padding:0 90px}
.quote{position:relative;padding-left:34px;border-bottom:1px solid rgba(255,255,255,.12);padding-bottom:18px}
.quote::before{content:"\201C";position:absolute;left:0;top:-14px;font-size:54px;color:rgba(255,255,255,.35);font-family:Georgia,serif}
.quote p{font-size:12px;line-height:1.65;color:#c7d1e0;margin-bottom:12px}
.quote cite{font-style:normal;font-size:12px;color:var(--green)}
.testimonials .center-cta{margin-top:46px}

.site-footer{height:220px;background:var(--footer);padding:58px 70px 0;color:var(--footer-text);font-size:12px}
.footer-row{display:flex;justify-content:space-between;align-items:center}
.footer-links a{color:var(--footer-text);text-decoration:none;margin-right:26px}
.socials{display:flex;gap:10px}
.socials span{width:32px;height:32px;border-radius:50%;border:1px solid var(--footer-text)}
.footer-note{margin-top:50px;border-top:1px solid #2e3238;padding-top:22px;font-size:11px}
</style>
</head>
<body>
<div class="page">

<header class="site-header">
  <div class="brand"><span class="brand-mark"></span><span class="brand-name">Clear Path Ledger</span></div>
  <div class="contact">
    <span class="contact-icon"><svg width="18" height="18" viewBox="0 0 24 24"><path fill="#fff" d="M6.6 10.8a15.1 15.1 0 0 0 6.6 6.6l2.2-2.2a1 1 0 0 1 1-.25 11.4 11.4 0 0 0 3.6.57 1 1 0 0 1 1 1V20a1 1 0 0 1-1 1A17 17 0 0 1 3 4a1 1 0 0 1 1-1h3.5a1 1 0 0 1 1 1c0 1.25.2 2.45.57 3.6a1 1 0 0 1-.25 1z"/></svg></span>
    <span>Contact Us On 1300 555 014</span>
  </div>
</header>

<nav class="main-nav">
  <a href="#">Home</a><a href="#">About us</a><a href="#">Debt Agreements</a><a href="#">Bad Credit Loans</a><a href="#">Consolidation Loans</a><a href="#">Get rid of Debt</a><a href="#">FAQ</a>
</nav>

<section class="hero">
  <div class="hero-photo" role="img" aria-label="Photograph of a person reviewing bills and paperwork at a desk"></div>
  <div class="hero-shade"></div>
  <div class="hero-copy">
    <h1>Looking To Consolidate Your Debts?</h1>
    <p>If you have over $10,000 in debt, we can help you get back on track. Clear Path Ledger is one of Australia's most trusted debt relief teams, working with lenders so you can repay in a way that suits you.</p>
    <p>Whether you are behind on payments or simply need a plan, our advisers look at your whole situation and find the best path forward. Talk to us today and take the first step toward a debt free future with expert help.</p>
  </div>
  <form class="consult-form">
    <h2>Free Consultation</h2>
    <p class="intro">Fill in the form below to receive your free, no obligation consultation.</p>
    <div class="field"><span>Name</span><i></i></div>
    <div class="field"><span>Phone</span><i></i></div>
    <div class="field"><span>Email</span><i></i></div>
    <div class="field"><span>Postcode</span><i></i></div>
    <div class="field"><span>Amount Owed</span><i></i></div>
    <div class="field"><span>Preferred Call Time</span><i></i></div>
    <span class="btn">GET MY FREE CONSULTATION</span>
  </form>
</section>

<section class="services">
  <h2 class="section-title">Here Are Just Some Of Our <em>Debt</em> Relief Services</h2>
  <div class="service-grid">
    <div class="service">
      <div class="service-icon"><svg width="28" height="28" viewBox="0 0 24 24" fill="none" stroke="#1b3257" stroke-width="2"><rect x="3" y="6" width="18" height="12" rx="2"/><circle cx="12" cy="12" r="2.5"/></svg></div>
      <h3>Debt Consolidation Loans</h3>
      <p>Combine your credit cards and personal loans into one simple repayment with a single, lower interest rate.</p>
    </div>
    <div class="service">
      <div class="service-icon"><svg width="28" height="28" viewBox="0 0 24 24" fill="none" stroke="#1b3257" stroke-width="2"><path d="M3 11l9-7 9 7"/><path d="M5 10v10h14V10"/></svg></div>
      <h3>Mortgage Refinance</h3>
      <p>Refinance your home loan to access a better rate, release equity and reduce your monthly repayments.</p>
    </div>
    <div class="service">
      <div class="service-icon"><svg width="28" height="28" viewBox="0 0 24 24" fill="none" stroke="#1b3257" stroke-width="2"><path d="M6 3h9l4 4v14H6z"/><path d="M9 12h7M9 16h7"/></svg></div>
      <h3>Debt Agreements</h3>
      <p>A formal arrangement with your creditors that lets you repay an affordable amount over a set period.</p>
    </div>
    <div class="service">
      <div class="service-icon"><svg width="28" height="28" viewBox="0 0 24 24" fill="none" stroke="#1b3257" stroke-width="2"><path d="M5 12l5 5 9-10"/></svg></div>
      <h3>Credit Repair</h3>
      <p>We help you correct errors on your credit file and rebuild your score so lenders see you in a better light.</p>
    </div>
    <div class="service">
      <div class="service-icon"><svg width="28" height="28" viewBox="0 0 24 24" fill="none" stroke="#1b3257" stroke-width="2"><path d="M12 3v18M4 8h16M7 8l-3 7h6zM17 8l-3 7h6z"/></svg></div>
      <h3>Bankruptcy</h3>
      <p>Clear advice on whether bankruptcy is right for you, and support through every step if it is the only option.</p>
    </div>
    <div class="service">
      <div class="service-icon"><svg width="28" height="28" viewBox="0 0 24 24" fill="none" stroke="#1b3257" stroke-width="2"><rect x="3" y="6" width="18" height="12" rx="2"/><path d="M3 10h18"/></svg></div>
      <h3>Bad Credit Loans</h3>
      <p>Had trouble in the past? We work with lenders who look beyond your credit history to your current situation.</p>
    </div>
  </div>
  <div class="center-cta"><span class="btn">GET MY FREE CONSULTATION</span></div>
</section>

<section class="testimonials">
  <h2 class="section-title">Here's What Our Valued <em>Customers</em> Have To Say About Us</h2>
  <div class="quote-grid">
    <div class="quote"><p>We were on the edge of losing our car and the bills kept piling up. The team sat down with us, explained our options and set up one payment we could actually afford each fortnight. We finally sleep at night again.</p><cite>Maree Tollan, NSW</cite></div>
    <div class="quote"><p>I was very nervous about calling but the adviser was friendly and never judged me. Within weeks my creditors stopped calling and I had a plan that fit my budget. I would recommend them to anyone.</p><cite>Kara Wendell, VIC</cite></div>
    <div class="quote"><p>I had five credit cards and no idea how to get out. They consolidated everything into one loan with a lower rate and I am now ahead for the first time in years. Great service from start to finish.</p><cite>Rory Pratten, QLD</cite></div>
    <div class="quote"><p>After my business closed I thought bankruptcy was my only option. They showed me a debt agreement instead and walked me through every form. Honest advice from people who care.</p><cite>Dale Morrow, WA</cite></div>
    <div class="quote"><p>Quick, clear and professional. They found a refinance deal that cut our mortgage repayments and cleared our personal loan. We have money left over each month and far less stress at home.</p><cite>Tessa Harlow, SA</cite></div>
    <div class="quote"><p>Thank you for helping me repair my credit file. Errors I did not know about were removed and I was approved for a car loan soon after. I am so glad I made the call.</p><cite>Lena Bramwell, TAS</cite></div>
  </div>
  <div class="center-cta"><span class="btn">GET MY FREE CONSULTATION</span></div>
</section>

<footer class="site-footer">
  <div class="footer-row">
    <div class="footer-links"><a href="#">Home</a><a href="#">About us</a><a href="#">Debt Agreements</a><a href="#">Privacy Policy</a><a href="#">Contact us</a><a href="#">Call 1300 555 014</a></div>
    <div class="socials"><span></span><span></span><span></span><span></span></div>
  </div>
  <p class="footer-note">© Clear Path Ledger · clearpathledger.com.au · All rights reserved.</p>
</footer>

</div>
</body>
</html>
```